BrackenLeaf Billboards

We already hava a logo, slogan and general theme, we are looking for 2 to 3 billboard designs for out Recreational-Use Retail Cannabis Dispensary in NY state. We would like for the billboard to be a "Space" theme with a realistic-looking astronaut, we cannot have any "cartoon-like" images that would be attractive to children per state regulations. We would like the following wording included:
BrackenLeaf Cannabis Company - Oswego , slogan is "Products out of this world" , address of 287 Harlow Street - Oswego, Free Delivery - Orders over $150 . Our primary brand color is lime green.

```html
<!DOCTYPE html>
<html lang="en">
<head>
<meta charset="utf-8">
<title>BrackenLeaf Cannabis Company – Billboard</title>
<link rel="stylesheet" href="https://fonts.googleapis.com/css2?family=Montserrat:wght@600;700;800&family=Poppins:wght@600;700&family=Syncopate:wght@700&display=swap">
<style>
  :root {
    --stage: #e6e6e6;
    --lime: #8cc63f;
    --white: #ffffff;
    --ink: #000000;
    --space-deep: #0a0d1c;
    --space-violet: #3a2566;
    --space-green: #1f5a2c;
    --space-orange: #9a5a2a;
    --box-fill: rgba(10, 14, 20, 0.75);
  }
  * { box-sizing: border-box; margin: 0; padding: 0; }
  html, body {
    width: 1200px; height: 486px; overflow: hidden;
    background: var(--stage);
  }
  .billboard {
    position: absolute; left: 70px; top: 89px;
    width: 1060px; height: 308px;
    overflow: hidden;
    box-shadow: 0 10px 24px rgba(0, 0, 0, 0.22);
    background:
      radial-gradient(ellipse 220px 160px at 80px 190px, var(--space-green), transparent 70%),
      radial-gradient(ellipse 260px 150px at 560px 170px, var(--space-violet), transparent 75%),
      radial-gradient(ellipse 200px 120px at 720px 210px, var(--space-orange), transparent 70%),
      var(--space-deep);
    font-family: "Montserrat", sans-serif;
    color: var(--white);
  }
  .scene-art {
    position: absolute; left: 754px; top: 63px; width: 306px; height: 180px;
    background: radial-gradient(ellipse 140px 90px at 60% 40%, #c0553a, #6a3a6a 55%, #1d4a55 85%, transparent 100%);
  }
  .brand {
    position: absolute; left: 34px; top: 36px; width: 236px;
    text-align: center; font-weight: 700; line-height: 1.15;
    color: var(--white);
  }
  .brand-name { font-size: 22px; }
  .brand-sub { font-size: 13px; letter-spacing: 0.5px; }
  .brand-rule { height: 1px; background: var(--white); margin: 4px 28px 4px; }
  .brand-town { font-size: 13px; letter-spacing: 1px; }
  .slogan {
    position: absolute; left: 300px; top: 34px;
    font-family: "Syncopate", sans-serif; font-weight: 700;
    font-size: 42px; line-height: 46px; letter-spacing: 1px;
  }
  .slogan-top { color: var(--lime); }
  .slogan-bottom { color: var(--white); }
  .delivery {
    position: absolute; left: 42px; top: 140px;
    font-weight: 800; line-height: 1;
  }
  .delivery-free { color: var(--lime); font-size: 64px; }
  .delivery-word { color: var(--white); font-size: 33px; margin-top: 2px; }
  .offer {
    position: absolute; left: 231px; top: 137px; width: 162px; height: 92px;
    border: 1.5px solid var(--lime); background: var(--box-fill);
    text-align: center; font-weight: 800;
  }
  .offer-label { color: var(--lime); font-size: 17px; margin-top: 7px; }
  .offer-amount { font-size: 52px; line-height: 56px; }
  .offer-amount sup { font-size: 26px; vertical-align: 20px; }
  .location {
    position: absolute; left: 432px; top: 156px;
    display: flex; gap: 10px;
    font-family: "Poppins", sans-serif; font-weight: 600;
  }
  .location-pin { width: 28px; height: 40px; margin-top: 4px; }
  .location-street { font-size: 29px; line-height: 34px; }
  .location-town { font-size: 29px; line-height: 34px; color: var(--lime); margin-left: 8px; }
  .contact-bar {
    position: absolute; left: 0; bottom: 0; width: 100%; height: 65px;
    background: var(--ink);
    display: flex; align-items: center; justify-content: space-between;
    padding: 0 38px 0 36px;
  }
  .contact-phone { font-size: 39px; font-weight: 600; }
  .contact-web { font-family: "Poppins", sans-serif; font-size: 40px; font-weight: 700; }
  .contact-web span { color: var(--lime); }
</style>
</head>
<body>
  <main class="billboard">
    <div class="scene-art" role="img" aria-label="Realistic astronaut floating in space above a glowing planet"></div>

    <div class="brand">
      <div class="brand-name">BrackenLeaf</div>
      <div class="brand-sub">Cannabis Company</div>
      <div class="brand-rule"></div>
      <div class="brand-town">Oswego</div>
    </div>

    <h1 class="slogan">
      <div class="slogan-top">PRODUCTS OUT OF</div>
      <div class="slogan-bottom">THIS WORLD</div>
    </h1>

    <div class="delivery">
      <div class="delivery-free">FREE</div>
      <div class="delivery-word">DELIVERY</div>
    </div>

    <div class="offer">
      <div class="offer-label">ORDERS OVER</div>
      <div class="offer-amount"><sup>$</sup>150</div>
    </div>

    <div class="location">
      <svg class="location-pin" viewBox="0 0 28 40" aria-hidden="true">
        <path d="M14 0C6.3 0 0 6.2 0 13.9 0 24.3 14 40 14 40s14-15.7 14-26.1C28 6.2 21.7 0 14 0z" fill="var(--lime)"/>
        <circle cx="14" cy="14" r="5.5" fill="var(--space-deep)"/>
      </svg>
      <div>
        <div class="location-street">287 Harlow Street</div>
        <div class="location-town">Oswego</div>
      </div>
    </div>

    <footer class="contact-bar">
      <div class="contact-phone">(315) 555-0148</div>
      <div class="contact-web">www.<span>brackenleaf</span>.com</div>
    </footer>
  </main>
</body>
</html>
```